Buff & Gleam

polished concrete and epoxy coatings flooring company

Target Market(s)

Industrial commercial

Industry/Entity Type

Industrial flooring contractor

Contact Information for Business Card

POLISHED CONCRETE • EPOXY COATING • TERRAZZO RESTORATION • SHOT BLASTING • SURFACE PREPARATION • JOINT FILLING • TILE/ CARPET /GLUE REMOVAL

Colors
0054AA
0677BA
7BADD7
CADEEF
E8F1F8

Requirements
Must have
• email buffandgleamfloors@mailnest.test Address 24593 Wendover Hwy, Fraser, MI 48031. Name Ray Tullin. Services Polished concrete- Epoxy Coatings- Terrazzo restoration-surface preparation- safety striping- joint filling- tile/ carpet/ glue removal phone number 586-555-0173 email buffandgleamfloors.test
Nice to have
• Instagram Facebook logo maybe smaller in the corner

```html
<!DOCTYPE html>
<html lang="en">
<head>
<meta charset="utf-8">
<title>Buff &amp; Gleam — Business Card</title>
<link rel="stylesheet" href="https://fonts.googleapis.com/css2?family=Open+Sans:wght@300;400;600;700&family=Oswald:wght@500&display=swap">
<style>
  :root {
    --page-bg: #d4d8d9;
    --card-bg: #222226;
    --ink: #ffffff;
    --ink-soft: #e9e9ea;
  }
  * { box-sizing: border-box; margin: 0; padding: 0; }
  html, body { width: 1200px; height: 960px; overflow: hidden; background: var(--page-bg); }
  body { position: relative; font-family: "Open Sans", sans-serif; color: var(--ink); }

  .card {
    position: absolute; left: 249px; width: 701px; height: 400px;
    background: var(--card-bg); border-radius: 24px; overflow: hidden;
  }
  .card--front { top: 60px; }
  .card--back { top: 500px; }

  .brand { position: absolute; text-align: center; }
  .brand__name {
    font-family: "Open Sans", sans-serif; font-weight: 600;
    font-size: 48px; line-height: 1.05; color: var(--ink); letter-spacing: 1px;
  }
  .brand__tagline {
    font-family: "Oswald", sans-serif; font-weight: 500;
    font-size: 19px; letter-spacing: 0.6px; color: var(--ink); margin-top: 14px;
  }
  .card--front .brand { left: 0; right: 0; top: 108px; }
  .card--back .brand { left: 24px; width: 236px; top: 58px; text-align: left; }
  .card--back .brand__name { font-size: 44px; line-height: 1.1; }
  .card--back .brand__tagline { font-size: 17px; margin-top: 16px; }

  .services { position: absolute; left: 0; right: 0; top: 300px; text-align: center; }
  .services__title { font-size: 16px; font-weight: 400; letter-spacing: 0.5px; margin-bottom: 4px; }
  .services__row { font-size: 15.6px; line-height: 25px; letter-spacing: 0.3px; color: var(--ink-soft); }
  .services__row span::before { content: "●"; font-size: 11px; margin: 0 6px 0 8px; vertical-align: 2px; }

  .holder { position: absolute; right: 24px; top: 22px; font-size: 37px; line-height: 1; }
  .holder__first { font-weight: 700; }
  .holder__last { font-weight: 300; }
  .holder-bar { position: absolute; right: 0; top: 25px; width: 15px; height: 43px; background: var(--ink); }

  .contact { position: absolute; left: 28px; top: 281px; list-style: none; }
  .contact li { display: flex; align-items: center; height: 22.3px; font-size: 16px; letter-spacing: 0.4px; color: var(--ink-soft); }
  .contact svg { width: 17px; height: 17px; margin-right: 10px; flex: none; }

  .social { position: absolute; right: 28px; top: 351px; display: flex; gap: 8px; }
  .social__dot { width: 18px; height: 18px; border-radius: 50%; background: var(--ink); }
</style>
</head>
<body>

<section class="card card--front">
  <div class="brand">
    <div class="brand__name">Buff &amp; Gleam</div>
    <div class="brand__tagline">INNOVATIVE CONCRETE FLOORING</div>
  </div>
  <div class="services">
    <div class="services__title">SERVICES</div>
    <div class="services__row"><span>Polished Concrete</span><span>Epoxy Coatings</span><span>Terrazzo Restoration</span></div>
    <div class="services__row"><span>Surface Preparation</span><span>Safety Striping</span><span>Joint Filling</span><span>Tile/ Carpet/ Glue Removal</span></div>
  </div>
</section>

<section class="card card--back">
  <div class="brand">
    <div class="brand__name">Buff &amp;<br>Gleam</div>
    <div class="brand__tagline">INNOVATIVE CONCRETE FLOORING</div>
  </div>

  <div class="holder"><span class="holder__first">Ray</span> <span class="holder__last">Tullin</span></div>
  <div class="holder-bar"></div>

  <ul class="contact">
    <li>
      <svg viewBox="0 0 24 24" fill="#fff"><path d="M6.6 2.5l3 3.2-1.8 2.4c1.3 2.9 3.4 5 6.2 6.2l2.4-1.8 3.2 3-1.5 3.1c-8.2-.5-14.6-6.9-15-15z"/></svg>
      586-555-0173
    </li>
    <li>
      <svg viewBox="0 0 24 24" fill="none" stroke="#fff" stroke-width="2"><circle cx="12" cy="12" r="9.5"/><path d="M2.5 12h19M12 2.5c3 3 3 16 0 19M12 2.5c-3 3-3 16 0 19"/></svg>
      www.buffandgleamfloors.test
    </li>
    <li>
      <svg viewBox="0 0 24 24" fill="none" stroke="#fff" stroke-width="2"><rect x="2.5" y="6" width="19" height="14" rx="1"/><path d="M2.5 7l9.5 7 9.5-7"/></svg>
      buffandgleamfloors@mailnest.test
    </li>
    <li>
      <svg viewBox="0 0 24 24" fill="none" stroke="#fff" stroke-width="2"><path d="M12 21s-6.5-6.6-6.5-11.5a6.5 6.5 0 0113 0C18.5 14.4 12 21 12 21z"/><circle cx="12" cy="9.5" r="2.4"/></svg>
      24593 Wendover Hwy, Fraser, MI 48031
    </li>
  </ul>

  <div class="social" aria-label="Social media links">
    <div class="social__dot"></div>
    <div class="social__dot"></div>
  </div>
</section>

</body>
</html>
```